Wordpress Design Project (Brantvik)

We need a wordpress design for an established auction and real estate company based in Minnesota. The winning design will incorporate the colors of logo (red white and black) creatively in a very professional and clean layout. Client mentions liking the site http://www.dornwellsales.example/ and http://www.tarpliconauction.example/ as a general idea for what they like.

Industry/Entity Type

Real Estate

Requirements
Must have
• Navigation:
1) Home - will have auction list, no text
2) Upcoming Auctions
3) Online Auctions
4) Real Estate
5) Auction Gallery
6) For Sale
7) About Us
8) Contact Us

Sidebar widget will include:
- email signup
- asset for sale fader (seen in Featured Listings at http://www.tarpliconauction.example/)
- Slideshow - initial image attached
- Video widget (image attached)
- social media icons for Youtube, Facebook, Twitter, LinkedIn and RSS feed
- testimonials

Footer will have smaller logo and contact info
Nice to have
• Nice to Have:
- use of drop-down menu design for 'About Us'
1) About Brantvik
2) Testimonials

```html
<!DOCTYPE html>
<html lang="en">
<head>
<meta charset="utf-8">
<title>Brantvik Auction &amp; Real Estate Services</title>
<link rel="stylesheet" href="https://fonts.googleapis.com/css2?family=Roboto+Condensed:ital,wght@0,400;0,700;1,700&family=Open+Sans:ital,wght@0,400;0,600;1,400;1,600&display=swap">
<style>
:root{
  --red:#9b2228;
  --red-dark:#7f1a1f;
  --ink:#222;
  --text:#666;
  --muted:#888;
  --page:#eeedeb;
  --white:#fff;
  --panel:#f3f3f3;
  --nav-top:#c68d5c;
  --nav-bot:#a8703f;
  --nav-text:#3a2414;
  --line:#d9d9d9;
}
*{box-sizing:border-box;margin:0;padding:0}
html,body{width:988px;height:1200px;overflow:hidden}
body{background:var(--page);font-family:"Open Sans",sans-serif;color:var(--text);position:relative}
.abs{position:absolute}
a{color:inherit;text-decoration:none}

/* header */
.site-header{position:absolute;left:0;top:0;width:988px;height:113px;background:var(--white)}
.brand{left:104px;top:24px;display:flex;align-items:center;gap:8px}
.brand-mark{width:22px;height:22px;background:var(--red)}
.brand-name{font-family:"Roboto Condensed",sans-serif;font-weight:700;font-size:36px;color:var(--red);letter-spacing:-.5px}
.brand-phone{left:104px;top:70px;font-family:"Roboto Condensed",sans-serif;font-weight:700;font-size:15px;color:var(--red)}
.tagline{left:300px;width:412px;top:20px;text-align:center;font-family:"Roboto Condensed",sans-serif;font-style:italic;font-weight:700;font-size:24px;color:var(--red)}
.header-phone{left:300px;width:412px;top:56px;text-align:center;font-family:"Roboto Condensed",sans-serif;font-style:italic;font-weight:700;font-size:23px;color:var(--ink)}
.auth{top:20px;display:flex;gap:8px;left:727px}
.auth a{display:block;height:30px;line-height:30px;border-radius:5px;background:linear-gradient(#fff,#e4e4e4);border-left:6px solid var(--red);border-right:6px solid var(--red);font-family:"Roboto Condensed",sans-serif;font-weight:700;font-size:14px;text-align:center}
.auth .login{width:68px;color:var(--ink)}
.auth .register{width:84px;color:var(--red)}
.social{left:726px;top:70px;display:flex;gap:5.5px}
.social span{width:22px;height:22px;border-radius:50%;background:linear-gradient(#9a9a9a,#6e6e6e)}

/* navigation */
.main-nav{left:0;top:113px;width:988px;height:41px;background:linear-gradient(var(--nav-top),var(--nav-bot))}
.main-nav ul{list-style:none;display:flex;margin-left:104px;height:41px}
.main-nav li{height:41px;line-height:41px;padding:0 16px;font-family:"Roboto Condensed",sans-serif;font-size:15px;color:var(--nav-text);border-right:1px solid rgba(0,0,0,.12)}
.main-nav li.active{background:var(--red);color:#fff}
.hero-band{left:0;top:154px;width:988px;height:258px;background:var(--red)}

/* content sheet */
.sheet{left:104px;top:175px;width:781px;height:847px;background:var(--white)}
.slide-photo{left:111px;top:182px;width:525px;height:294px;background:linear-gradient(135deg,#3f7a2e,#6a6a5a 45%,#2f6a2a 70%,#8a5a48)}
.slide-title{left:658px;top:199px;width:224px;font-family:"Roboto Condensed",sans-serif;font-weight:700;font-size:24px;line-height:31px;letter-spacing:-.3px;color:var(--red)}
.slide-price{left:659px;top:274px;font-family:"Roboto Condensed",sans-serif;font-size:23px;color:var(--ink)}
.slide-text{left:659px;top:315px;width:215px;font-size:10.5px;line-height:19px;color:var(--muted)}
.slide-btn{left:659px;top:393px}
.dots{left:660px;top:447px;display:flex;gap:5px}
.dots span{width:11px;height:11px;border-radius:50%;background:#ddd}
.dots span.on{background:var(--red)}
.slide-shadow{left:110px;top:483px;width:770px;height:8px;background:radial-gradient(ellipse at top,rgba(0,0,0,.18),transparent 70%)}

.welcome-title{left:119px;top:509px;font-family:"Roboto Condensed",sans-serif;font-weight:700;font-size:20px;color:var(--red)}
.dotted{left:119px;top:541px;width:491px;border-top:4px dotted #ddd}
.welcome-text{left:119px;top:553px;width:492px;font-size:10.2px;line-height:17.3px;text-align:justify;color:var(--muted)}
.read-more{left:562px;top:684px;font-size:9px;font-style:italic;font-weight:600;color:var(--red)}
.video{left:635px;top:514px;width:235px;height:178px;background:#fff;box-shadow:0 0 4px rgba(0,0,0,.3);padding:4px}
.video-screen{width:227px;height:170px;background:linear-gradient(#2a2a2a,#8b2226 35%,#c8c8c8 60%,#111 92%);position:relative}
.video-title{position:absolute;left:11px;top:10px;font-size:11px;font-weight:600;color:#fff}

/* feature boxes */
.box{top:723px;width:234px;height:275px;background:var(--panel);border:1px solid #ddd;border-radius:4px;overflow:hidden}
.box-head{height:34px;line-height:34px;background:var(--red);color:#fff;font-family:"Roboto Condensed",sans-serif;font-weight:700;font-size:16px;padding-left:15px}
.box-sub{margin:10px 0 0 15px;font-family:"Roboto Condensed",sans-serif;font-weight:700;font-size:13px;color:#444}
.box-photo{margin:10px 0 0 16px;width:203px;height:117px;border:3px solid #fff;box-shadow:0 0 3px rgba(0,0,0,.4)}
.box-meta{margin:10px 0 0 15px;font-style:italic;font-weight:600;font-size:10px;line-height:19px;color:#555}
.box-meta .date{font-size:11px}
.quote{position:relative;padding:12px 10px 0 16px;height:120px}
.quote+.quote{border-top:1px solid #ddd;background:linear-gradient(#e6e6e6,#f3f3f3 12px)}
.quote p{font-size:10.2px;line-height:17px;color:var(--muted);text-indent:24px}
.quote .mark{position:absolute;left:15px;top:8px;font-family:"Roboto Condensed",sans-serif;font-weight:700;font-size:34px;line-height:34px;color:#ccc}
.quote .who{margin-top:8px;font-style:italic;font-weight:600;font-size:12px;line-height:16px;color:var(--red)}
.corner{position:absolute;right:0;bottom:0}

/* footer */
.map{left:118px;top:1046px;width:170px;height:115px;border:3px solid #fff;box-shadow:0 0 3px rgba(0,0,0,.3);background:linear-gradient(135deg,#e8e4dc,#dcd7cc)}
.contact-title{left:302px;top:1040px;font-family:"Roboto Condensed",sans-serif;font-weight:700;font-size:22px;color:var(--red)}
.contact{left:302px;top:1069px;font-size:10px;line-height:15px;color:#555}
.contact hr{border:0;border-top:1px solid #ccc;width:86px;margin:4px 0}
.contact .ind{padding-left:10px}
.contact .email{margin-top:7px}
.vrule{top:1040px;width:1px;height:130px;background:#d4d4d4}
.footer-nav{left:530px;top:1046px;list-style:none;font-size:10px;line-height:18.8px;color:#555}
.footer-nav li::before{content:"›";margin-right:5px}
.footer-brand{left:700px;top:1080px;display:flex;align-items:center;gap:7px}
.footer-brand .brand-name{font-size:32px}
.footer-phone{left:700px;top:1120px;font-family:"Roboto Condensed",sans-serif;font-weight:700;font-size:14px;color:var(--red)}
.copyright{left:711px;top:1176px;font-size:10px;color:#777}
</style>
</head>
<body>

<header class="site-header">
  <div class="abs brand"><span class="brand-mark"></span><span class="brand-name">Brantvik</span></div>
  <div class="abs brand-phone">555-014-2870</div>
  <div class="abs tagline">Autction &amp; Real Estate Services</div>
  <div class="abs header-phone">555-014-2870</div>
  <div class="abs auth"><a class="login" href="#">Login</a><a class="register" href="#">Register</a></div>
  <div class="abs social" aria-label="Social links"><span></span><span></span><span></span><span></span><span></span><span></span></div>
</header>

<nav class="abs main-nav">
  <ul>
    <li class="active">Home</li><li>About Us</li><li>Upcoming Auctions</li><li>Online Auctions</li><li>Real Estate</li><li>Auction Gallery</li><li>For Sale</li><li>Contact Us</li>
  </ul>
</nav>
<div class="abs hero-band"></div>

<main>
  <div class="abs sheet"></div>
  <div class="abs slide-photo" role="img" aria-label="Crowd at an outdoor farm equipment auction among green tractors"></div>
  <h1 class="abs slide-title">Lorem ipsum dolor sit amet consectetur</h1>
  <div class="abs slide-price">$ 0.000.0000</div>
  <p class="abs slide-text">Lorem ipsum dolor sit amet, consectetur adipisicing elit, sed do eiusmod tempor incididunt ut labore et dolore.</p>
  <svg class="abs slide-btn" width="136" height="30" viewBox="0 0 136 30">
    <path d="M0 0H122L136 15L122 30H0Z" fill="#9b2228"/>
    <text x="15" y="20" font-family="Open Sans, sans-serif" font-size="13" font-weight="600" fill="#fff">Read more Detail</text>
  </svg>
  <div class="abs dots"><span class="on"></span><span></span><span></span><span></span><span></span><span></span></div>
  <div class="abs slide-shadow"></div>

  <h2 class="abs welcome-title">Welcome to out site!</h2>
  <div class="abs dotted"></div>
  <p class="abs welcome-text">Lorem ipsum dolor sit amet, consectetur adipiscing elit. Donec mauris mi, mattis ac condimentum ullamcorper, consectetur eu lectus. Duis congue varius lacus, cursus luctus magna dignissim sit amet. Integer cursus sed mauris a convallis. Cras scelerisque arcu purus, at tempor quam congue id. Donec luctus risus eu enim vulputate suscipit. Nam gravida ac libero non viverra. Pellentesque quam lorem, ullamcorper sit amet pellentesque ut, pellentesque nec nisi. Nullam mollis nunc porta ligula rhoncus, ac lacinia lorem hendrerit. Aenean ac blandit mauris. Pellentesque sodales et felis et hendrerit. Vivamus ultrices nisl quis ligula sodales, et facilisis erat auctor. Ut nec vulputate lacus.</p>
  <a class="abs read-more" href="#">Read more...</a>

  <div class="abs video">
    <div class="video-screen" role="img" aria-label="Video still of an online bidding screen tutorial">
      <div class="video-title">Brantvik Bidder Tutorial.mp4</div>
      <svg style="position:absolute;left:97px;top:72px" width="34" height="34" viewBox="0 0 34 34"><circle cx="17" cy="17" r="16" fill="rgba(255,255,255,.35)" stroke="#fff" stroke-width="2"/><path d="M13 10L25 17L13 24Z" fill="#fff"/></svg>
    </div>
  </div>

  <section class="abs box" style="left:118px">
    <div class="box-head">Featured Auctions:</div>
    <div class="box-sub">Farmer Dealer Auction</div>
    <div class="box-photo" role="img" aria-label="Row of yellow loaders and equipment in snow" style="background:linear-gradient(#b9c4d4,#8a8a78 55%,#e6e8ec 70%)"></div>
    <div class="box-meta"><div class="date">Wednesday, August 14,2013 - 10:00 AM</div><div>48 Alder St N.Halvik, MN</div><div>West Central MN Farmer Dealer Equipment</div></div>
    <svg class="corner" width="30" height="30" viewBox="0 0 30 30"><path d="M30 0V30H0Z" fill="#9b2228"/><circle cx="21" cy="21" r="3" fill="none" stroke="#fff" stroke-width="1.5"/></svg>
  </section>

  <section class="abs box" style="left:377px">
    <div class="box-head">Testimonial</div>
    <div class="quote"><span class="mark">“</span><p>Lorem ipsum dolor met, consectetur adipiscing elit. Donec mauris mi, mattis ac Lorem ipsum dolor sit amet, consectetur adipiscing elit. Donec</p><div class="who">Halvik, MN</div></div>
    <div class="quote"><span class="mark">“</span><p>Lorem ipsum dolor met, consectetur adipiscing elit. Donec mauris mi, mattis ac Lorem ipsum dolor sit amet, consectetur adipiscing elit. Donec</p><div class="who">Halvik, MN</div></div>
    <svg class="corner" width="30" height="30" viewBox="0 0 30 30"><path d="M30 0V30H0Z" fill="#9b2228"/><circle cx="21" cy="21" r="3" fill="none" stroke="#fff" stroke-width="1.5"/></svg>
  </section>

  <section class="abs box" style="left:635px">
    <div class="box-head">Featured Listings:</div>
    <div class="box-sub">Farmer Dealer Consignmentuction</div>
    <div class="box-photo" role="img" aria-label="Green tractors with bidders at an auction yard" style="background:linear-gradient(135deg,#6b5a48,#3f7a2e 50%,#7a6a58)"></div>
    <div class="box-meta"><div class="date">Wednesday, August 14,2013 - 10:00 AM</div><div>48 Alder St N.Halvik, MN</div><div>West Central MN Farmer Dealer Equipment</div></div>
    <svg class="corner" width="30" height="30" viewBox="0 0 30 30"><path d="M30 0V30H0Z" fill="#9b2228"/><circle cx="21" cy="21" r="3" fill="none" stroke="#fff" stroke-width="1.5"/></svg>
  </section>
</main>

<footer>
  <div class="abs map" role="img" aria-label="Street map showing the office location"></div>
  <h3 class="abs contact-title">Contact Us</h3>
  <div class="abs contact">
    <div>48 Alder Street North Halvik,</div>
    <div>MN&nbsp; 56999</div>
    <hr>
    <div>Office: 555-014-2870</div>
    <div class="ind">Call: 555-017-3391</div>
    <div class="ind">Fax: 555-019-4402</div>
    <hr>
    <div class="email">Email: info@brantvikauctions.example</div>
  </div>
  <div class="abs vrule" style="left:490px"></div>
  <ul class="abs footer-nav">
    <li>Home</li><li>About Us</li><li>Upcoming Auctions</li><li>Online Auctions</li><li>Real Estate</li><li>Auction Gallery</li><li>For Sale</li><li>Contact Us</li>
  </ul>
  <div class="abs vrule" style="left:662px"></div>
  <div class="abs footer-brand"><span class="brand-mark"></span><span class="brand-name">Brantvik</span></div>
  <div class="abs footer-phone">555-014-2870</div>
  <div class="abs copyright">(c)2013 Brantvik. All rights reserved</div>
</footer>

</body>
</html>
```